NEW Modern Sleek Business Card for VR Language Startup

Our startup is using VR to lead the next wave of world language education. We need a two-sided business card that introduces the larger organization (Brightvale Tongues Inc) and our contact info on one side and shows the product, Lexiquorra, on the other side.

Side 1 (contact info)= Brightvale Logo and Contact info (name, title, phone, email)

Side 2 (product)= Lexiquora logo, text, and website
Text= Culturally Immersive Language Learning Games
Website= www.lexiquora-demo.test

Target Market(s)

Education, Technology

Contact Information for Business Card

Contact info will be updated upon approval of the design. For now, put this as a placeholder.

Peter Hallow
Founder & CEO
phallow@mailbox-demo.test
(555)-010-4477

Font styles to use
Other font styles liked:
• Gibson and Century Gothic are the brand fonts

Requirements
Nice to have
• I would love to see cohesion between the design and colors of the two logos. I have attached a few business card designs that I like, so you can get a feel for my preferred style.

```html
<!DOCTYPE html>
<html lang="en">
<head>
<meta charset="utf-8">
<title>Brightvale Tongues – Business Card</title>
<link rel="stylesheet" href="https://fonts.googleapis.com/css2?family=Questrial&family=Roboto:wght@400;500;700&display=swap">
<style>
  :root {
    --backdrop: #b9bfc0;
    --card: #f4f4f2;
    --card-edge: #1f8fb0;
    --ink: #1d1d1f;
    --ink-soft: #444448;
    --name-blue: #2f9de8;
    --title-orange: #f47b20;
    --accent-blue: #2f4fd8;
    --accent-line: #4660e0;
  }
  * { box-sizing: border-box; margin: 0; padding: 0; }
  html, body {
    width: 1200px; height: 824px; overflow: hidden;
    background: var(--backdrop);
  }
  .sheet {
    width: 1200px; height: 824px;
    display: flex; align-items: center; justify-content: center; gap: 40px;
  }
  .card {
    position: relative;
    width: 540px; height: 309px;
    background: var(--card);
    border-bottom: 6px solid var(--card-edge);
    box-shadow: 0 10px 24px rgba(0,0,0,0.18);
    font-family: "Roboto", sans-serif;
  }

  /* Side 1 – contact */
  .contact {
    position: absolute; left: 40px; bottom: 70px;
  }
  .contact-name {
    font-family: "Roboto", sans-serif; font-weight: 500;
    font-size: 24px; color: var(--name-blue); line-height: 1.1;
  }
  .contact-title {
    font-size: 16px; font-weight: 500; color: var(--title-orange);
    margin-top: 2px;
  }
  .contact-line {
    font-size: 14px; color: var(--ink-soft); margin-top: 6px;
  }
  .contact-line b { color: var(--ink); font-weight: 700; }
  .org-mark {
    position: absolute; right: 44px; top: 110px;
    display: flex; align-items: center; gap: 12px;
  }
  .org-mark .dot {
    width: 26px; height: 26px; border-radius: 50%;
    background: var(--title-orange);
  }
  .org-name {
    font-family: "Questrial", sans-serif;
    font-size: 30px; color: var(--ink); letter-spacing: 3px;
  }

  /* Side 2 – product */
  .product {
    position: absolute; inset: 0;
    display: flex; flex-direction: column; align-items: center; justify-content: center;
  }
  .product-mark {
    display: flex; align-items: center; gap: 12px;
  }
  .product-mark .dot {
    width: 26px; height: 26px; border-radius: 50%;
    background: var(--accent-blue);
  }
  .product-name {
    font-family: "Questrial", sans-serif;
    font-size: 40px; color: var(--ink);
  }
  .tagline {
    margin-top: 10px;
    font-size: 13px; font-weight: 700; color: var(--ink);
  }
  .web-row {
    margin-top: 10px; display: flex; align-items: center; gap: 8px;
  }
  .web-row svg { display: block; }
  .web {
    font-size: 13px; color: var(--accent-blue);
  }
</style>
</head>
<body>
<main class="sheet">
  <section class="card card-contact" aria-label="Contact side">
    <div class="contact">
      <p class="contact-name">Peter Hallow</p>
      <p class="contact-title">Founder &amp; CEO</p>
      <p class="contact-line"><b>P:</b> (555)-010-4477 <b>E:</b> phallow@mailbox-demo.test</p>
    </div>
    <div class="org-mark">
      <span class="dot"></span>
      <span class="org-name">Brightvale</span>
    </div>
  </section>

  <section class="card card-product" aria-label="Product side">
    <div class="product">
      <div class="product-mark">
        <span class="dot"></span>
        <span class="product-name">Lexiquora</span>
      </div>
      <p class="tagline">Culturally Immersive Language Learning Games</p>
      <div class="web-row">
        <svg width="100" height="8" viewBox="0 0 100 8" aria-hidden="true">
          <line x1="0" y1="4" x2="94" y2="4" stroke="var(--accent-line)" stroke-width="1"/>
          <circle cx="96" cy="4" r="3" fill="none" stroke="var(--accent-line)" stroke-width="1.2"/>
        </svg>
        <span class="web">www.lexiquora-demo.test</span>
        <svg width="100" height="8" viewBox="0 0 100 8" aria-hidden="true">
          <circle cx="4" cy="4" r="3" fill="none" stroke="var(--accent-line)" stroke-width="1.2"/>
          <line x1="6" y1="4" x2="100" y2="4" stroke="var(--accent-line)" stroke-width="1"/>
        </svg>
      </div>
    </div>
  </section>
</main>
</body>
</html>
```